"Paint the river slow" My third R&B album release

I have photos for the front and back of the CD jacket and disc. I would like to get an original concept of some kind from the designer... My photo as a child on the front and disc. One of the other photos on the back. I'll let you play with textures and such as your vision see fit! This is my third commercial release, so be AWESOME!!!

R&B Lovers. Ages 30-55

Script

Designer to choose colors to be used in the design.

• The Logo below on the back of the disc to represent the record company.

```html
<!DOCTYPE html>
<html lang="en">
<head>
<meta charset="utf-8">
<title>Paint the river slow – CD jacket and disc</title>
<link rel="stylesheet" href="https://fonts.googleapis.com/css2?family=Open+Sans:wght@400;700&family=Parisienne&display=swap">
<style>
  :root {
    --page: #ffffff;
    --back-light: #f8f1b8;
    --back-mid: #f1e27a;
    --back-sun: #f6ea6a;
    --back-shade: #7a6640;
    --back-dark: #3e3322;
    --front-brick: #8a4a2a;
    --front-deep: #5a3a24;
    --front-amber: #d98a22;
    --front-glow: #f0c040;
    --front-leaf: #b8c060;
    --front-wash: #efe6da;
    --title-cream: #f4e9a2;
    --ink: #1d1a14;
    --disc-pale: #dfe6ee;
    --disc-cool: #a3b1c0;
    --disc-deep: #4f5d6e;
    --disc-hub: #e6e6e6;
    --ring-green: #5fa34a;
    --fold-red: #d23a3a;
  }
  html, body {
    margin: 0;
    padding: 0;
    overflow: hidden;
    background: var(--page);
  }
  .canvas {
    display: block;
    width: 1200px;
    height: 1200px;
  }
  .sans { font-family: "Open Sans", sans-serif; }
  .script { font-family: "Parisienne", cursive; }
  .back-heading { font-size: 14px; font-weight: 700; fill: var(--ink); }
  .back-track { font-size: 14px; fill: var(--ink); }
  .back-credit { font-size: 12.5px; fill: var(--ink); }
  .label-name { font-weight: 700; letter-spacing: 0.5px; }
  .back-label { font-size: 13px; fill: var(--ink); }
  .disc-label { font-size: 18px; fill: #ffffff; }
  .front-title { font-size: 52px; fill: var(--title-cream); }
  .front-artist { font-size: 54px; fill: var(--title-cream); }
  .disc-title { font-size: 42px; fill: var(--title-cream); }
  .disc-track { font-size: 14.5px; fill: #ffffff; }
  .disc-artist { font-size: 60px; fill: var(--title-cream); }
</style>
</head>
<body>
<svg class="canvas" viewBox="0 0 1200 1200" xmlns="http://www.w3.org/2000/svg">
  <defs>
    <linearGradient id="backGrad" x1="0" y1="0" x2="1" y2="0">
      <stop offset="0" stop-color="var(--back-light)"/>
      <stop offset="1" stop-color="var(--back-mid)"/>
    </linearGradient>
    <linearGradient id="backPhotoGrad" x1="0" y1="0" x2="1" y2="0">
      <stop offset="0" stop-color="#f4ea9a"/>
      <stop offset="0.45" stop-color="var(--back-sun)"/>
      <stop offset="1" stop-color="#e9cf5a"/>
    </linearGradient>
    <linearGradient id="frontBase" x1="0" y1="0" x2="1" y2="1">
      <stop offset="0" stop-color="var(--front-deep)"/>
      <stop offset="0.35" stop-color="var(--front-brick)"/>
      <stop offset="0.7" stop-color="var(--front-amber)"/>
      <stop offset="1" stop-color="#c9a050"/>
    </linearGradient>
    <linearGradient id="frontWashTop" x1="0" y1="0" x2="0" y2="1">
      <stop offset="0" stop-color="var(--front-wash)" stop-opacity="0.85"/>
      <stop offset="1" stop-color="var(--front-wash)" stop-opacity="0"/>
    </linearGradient>
    <linearGradient id="frontWashBottom" x1="0" y1="1" x2="0" y2="0">
      <stop offset="0" stop-color="#ffffff" stop-opacity="0.9"/>
      <stop offset="1" stop-color="#ffffff" stop-opacity="0"/>
    </linearGradient>
    <radialGradient id="discGrad" cx="0.62" cy="0.62" r="0.75">
      <stop offset="0" stop-color="var(--disc-pale)"/>
      <stop offset="0.55" stop-color="var(--disc-cool)"/>
      <stop offset="1" stop-color="var(--disc-deep)"/>
    </radialGradient>
    <filter id="blurSoft" x="-50%" y="-50%" width="200%" height="200%">
      <feGaussianBlur stdDeviation="28"/>
    </filter>
    <filter id="blurWide" x="-50%" y="-50%" width="200%" height="200%">
      <feGaussianBlur stdDeviation="45"/>
    </filter>
    <filter id="softShadow" x="-10%" y="-10%" width="120%" height="120%">
      <feDropShadow dx="0" dy="2" stdDeviation="4" flood-color="#000" flood-opacity="0.25"/>
    </filter>
    <clipPath id="backPhotoClip"><rect x="288" y="99" width="326" height="514"/></clipPath>
    <clipPath id="frontClip"><rect x="614" y="86" width="532" height="540"/></clipPath>
    <clipPath id="discClip"><circle cx="380" cy="902" r="270"/></clipPath>
  </defs>

  <!-- Sleeve flaps -->
  <g class="sleeve-flaps">
    <polygon points="614,86 632,26 1128,26 1146,86" fill="#ffffff" stroke="var(--fold-red)" stroke-width="1"/>
    <polygon points="614,626 1146,626 1128,688 632,688" fill="#ffffff" stroke="var(--fold-red)" stroke-width="1"/>
  </g>

  <!-- Back cover -->
  <g class="back-cover" filter="url(#softShadow)">
    <rect x="85" y="99" width="529" height="514" fill="url(#backGrad)"/>
  </g>
  <g class="back-photo" clip-path="url(#backPhotoClip)" role="img" aria-label="Photo of the singer in a hat and patterned shirt leaning against a sunlit wall">
    <rect x="288" y="99" width="326" height="514" fill="url(#backPhotoGrad)"/>
    <ellipse cx="330" cy="360" rx="55" ry="260" fill="#fbf6c8" opacity="0.8" filter="url(#blurSoft)"/>
    <ellipse cx="410" cy="180" rx="70" ry="45" fill="var(--back-dark)" opacity="0.75" filter="url(#blurSoft)"/>
    <ellipse cx="460" cy="440" rx="95" ry="190" fill="var(--back-shade)" opacity="0.7" filter="url(#blurWide)"/>
    <ellipse cx="440" cy="590" rx="70" ry="60" fill="var(--back-dark)" opacity="0.6" filter="url(#blurSoft)"/>
    <ellipse cx="585" cy="200" rx="60" ry="110" fill="#f0dc70" opacity="0.7" filter="url(#blurSoft)"/>
  </g>
  <line x1="288" y1="99" x2="288" y2="613" stroke="#8a7d4c" stroke-width="1"/>

  <g class="back-text sans">
    <text class="back-heading" x="107" y="164">PAINT THE RIVER SLOW</text>
    <g class="back-track">
      <text x="115" y="225">1. Song number 1</text>
      <text x="115" y="242.5">2. Song number 2</text>
      <text x="115" y="260">3. Song number 3</text>
      <text x="115" y="277.5">4. Song number 4</text>
      <text x="115" y="295">5. Song number 5</text>
      <text x="115" y="312.5">6. Song number 6</text>
      <text x="115" y="330">7. Song number 7</text>
      <text x="115" y="347.5">8. Song number 8</text>
      <text x="115" y="365">9. Song number 9</text>
      <text x="107" y="382.5">10. Song number 10</text>
      <text x="107" y="400">11. Song number 11</text>
      <text x="107" y="417.5">12. Song number 12</text>
      <text x="107" y="435">13. Song number 13</text>
      <text x="107" y="452.5">14. Song number 14</text>
    </g>
    <g class="back-credit">
      <text x="108" y="519">Credits musics band rights music band</text>
      <text x="108" y="535">Credits musics band rights music band</text>
      <text x="108" y="551">Credits musics band rights music band</text>
    </g>
    <g class="label-mark">
      <text class="label-name back-label" x="103" y="584">ORLEAN</text>
      <circle cx="168" cy="579" r="5" fill="var(--ink)"/>
    </g>
  </g>

  <!-- Front cover -->
  <g class="front-cover" filter="url(#softShadow)">
    <rect x="614" y="86" width="532" height="540" fill="var(--front-amber)"/>
  </g>
  <g class="front-photo" clip-path="url(#frontClip)" role="img" aria-label="Painted childhood photo of the singer as a boy posing against a brick wall">
    <rect x="614" y="86" width="532" height="540" fill="url(#frontBase)"/>
    <ellipse cx="700" cy="300" rx="110" ry="200" fill="#9a5436" opacity="0.8" filter="url(#blurWide)"/>
    <ellipse cx="860" cy="330" rx="110" ry="150" fill="#e9dc9a" opacity="0.55" filter="url(#blurWide)"/>
    <ellipse cx="880" cy="470" rx="160" ry="90" fill="var(--front-glow)" opacity="0.8" filter="url(#blurWide)"/>
    <ellipse cx="1090" cy="420" rx="90" ry="140" fill="var(--front-wash)" opacity="0.7" filter="url(#blurWide)"/>
    <ellipse cx="1100" cy="520" rx="70" ry="70" fill="var(--front-leaf)" opacity="0.6" filter="url(#blurSoft)"/>
    <ellipse cx="860" cy="560" rx="60" ry="50" fill="#3e3022" opacity="0.45" filter="url(#blurSoft)"/>
    <rect x="614" y="86" width="532" height="70" fill="url(#frontWashTop)"/>
    <rect x="614" y="566" width="532" height="60" fill="url(#frontWashBottom)"/>
  </g>
  <g class="front-text">
    <text class="script front-title" x="1116" y="194" text-anchor="end">Paint the</text>
    <text class="script front-title" x="1116" y="250" text-anchor="end">river slow</text>
    <text class="sans front-artist" x="1121" y="574" text-anchor="end">TAVIO</text>
  </g>

  <!-- Disc -->
  <g class="disc">
    <g clip-path="url(#discClip)" role="img" aria-label="Blue-toned childhood photo of the singer as a boy by a brick wall">
      <circle cx="380" cy="902" r="270" fill="url(#discGrad)"/>
      <ellipse cx="200" cy="820" rx="120" ry="140" fill="#5e6a78" opacity="0.7" filter="url(#blurWide)"/>
      <ellipse cx="310" cy="720" rx="60" ry="60" fill="#3f4854" opacity="0.6" filter="url(#blurSoft)"/>
      <ellipse cx="280" cy="1050" rx="60" ry="110" fill="#4e5a68" opacity="0.55" filter="url(#blurSoft)"/>
      <ellipse cx="560" cy="980" rx="110" ry="120" fill="#eef2f6" opacity="0.7" filter="url(#blurWide)"/>
      <ellipse cx="560" cy="760" rx="90" ry="60" fill="#7a8796" opacity="0.5" filter="url(#blurSoft)"/>
    </g>
    <circle cx="380" cy="902" r="264" fill="none" stroke="var(--ring-green)" stroke-width="1.5"/>
    <circle cx="380" cy="902" r="108" fill="none" stroke="var(--ring-green)" stroke-width="1.5"/>
    <circle cx="380" cy="902" r="99" fill="var(--disc-hub)"/>
    <circle cx="380" cy="902" r="34" fill="#ffffff" stroke="#555" stroke-width="1"/>

    <text class="script disc-title" x="552" y="735" text-anchor="end">Paint the</text>
    <text class="script disc-title" x="552" y="779" text-anchor="end">river slow</text>

    <g class="sans disc-track">
      <text x="258" y="845" text-anchor="end">1. Song number 1</text>
      <text x="254" y="864.5" text-anchor="end">2. Song number 2</text>
      <text x="250" y="884" text-anchor="end">3. Song number 3</text>
      <text x="247" y="903.5" text-anchor="end">4. Song number 4</text>
      <text x="250" y="923" text-anchor="end">5. Song number 5</text>
      <text x="254" y="942.5" text-anchor="end">6. Song number 6</text>
      <text x="258" y="962" text-anchor="end">7. Song number 7</text>

      <text x="478" y="845">8. Song number 8</text>
      <text x="486" y="864.5">9. Song number 9</text>
      <text x="494" y="884">10. Song number 10</text>
      <text x="498" y="903.5">11. Song number 11</text>
      <text x="494" y="923">12. Song number 12</text>
      <text x="490" y="942.5">13. Song number 13</text>
      <text x="482" y="962">14. Song number 14</text>
    </g>

    <text class="sans disc-artist" x="196" y="1071">TAVIO</text>
    <g class="label-mark">
      <text class="sans label-name disc-label" x="446" y="1053">ORLEAN</text>
      <circle cx="540" cy="1047" r="6.5" fill="#ffffff"/>
    </g>
  </g>
</svg>
</body>
</html>
```